Title: “The Lantern Path, Rebuilding The Spirit of Harbors, A Sailor’s Journal”

Cover design for ebook and printable book. Looking for this specific designer

```html
<!DOCTYPE html>
<html lang="en">
<head>
<meta charset="utf-8">
<title>The Lantern Path — Book Cover</title>
<link rel="stylesheet" href="https://fonts.googleapis.com/css2?family=Cinzel:wght@400;500&display=swap">
<style>
  :root {
    --paper: #ffffff;
    --ink: #0a0608;
    --accent-red: #c0211a;
    --art-red: #ee2a24;
    --art-red-deep: #d8221d;
  }
  html, body {
    margin: 0;
    padding: 0;
    background: var(--paper);
    overflow: hidden;
  }
  .cover {
    position: relative;
    width: 761px;
    height: 1200px;
    background: var(--paper);
    overflow: hidden;
    font-family: "Cinzel", "Trajan Pro", serif;
    color: var(--ink);
  }
  .cover__subtitle {
    position: absolute;
    top: 34px;
    left: 0;
    width: 100%;
    margin: 0;
    text-align: center;
    font-weight: 400;
    font-size: 42px;
    line-height: 54px;
    letter-spacing: 0.04em;
    white-space: nowrap;
  }
  .cover__tagline {
    position: absolute;
    top: 152px;
    left: 0;
    width: 100%;
    margin: 0;
    text-align: center;
    font-weight: 500;
    font-size: 26px;
    line-height: 30px;
    letter-spacing: 0.08em;
    color: var(--accent-red);
  }
  .cover__title {
    position: absolute;
    top: 198px;
    left: 0;
    width: 100%;
    margin: 0;
    text-align: center;
    font-weight: 400;
    font-size: 114px;
    line-height: 134px;
    letter-spacing: 0.01em;
  }
  .cover__title span { display: block; }
  .cover__art {
    position: absolute;
    top: 636px;
    left: 185px;
    width: 395px;
    height: 376px;
  }
  .cover__author {
    position: absolute;
    top: 1104px;
    left: 0;
    width: 100%;
    margin: 0;
    text-align: center;
    font-weight: 400;
    font-size: 56px;
    line-height: 64px;
    letter-spacing: 0.32em;
    text-indent: 0.32em;
  }
</style>
</head>
<body>
  <main class="cover">
    <p class="cover__subtitle">Rebuilding the Spirit<br>of Harbors</p>
    <p class="cover__tagline">A Sailor’s Journal</p>
    <h1 class="cover__title">
      <span>The</span>
      <span>Lantern</span>
      <span>Path</span>
    </h1>
    <svg class="cover__art" viewBox="0 0 395 376" role="img" aria-label="Illustration of two hands gently holding a red anatomical heart">
      <defs>
        <linearGradient id="artTone" x1="0" y1="0" x2="0" y2="1">
          <stop offset="0" stop-color="var(--art-red)"/>
          <stop offset="1" stop-color="var(--art-red-deep)"/>
        </linearGradient>
      </defs>
      <rect x="0" y="0" width="395" height="376" rx="28" fill="url(#artTone)"/>
    </svg>
    <p class="cover__author">Author Name</p>
  </main>
</body>
</html>
```